Cafe Menu for Maplebrook Lantern Cafe

Menu designed for my cafe. I need multiple sizes to be created.
DL pamphlet
A4
and I also need 5 x A3 portraits & 5 x A3 landscapes. The menu must be spread out over a total of 10 A3 pages. I have uploaded my logo which needs to be used & I would like the colours from the logo used. The background of the menu needs to be white. I have uploaded an image on another menu for which I would like the same heading font to be used.

Target Market(s)

cafe, restaurant

Font styles to use
Serif
Decorative
Script

Requirements
Must have
• White back ground
correct font as I have uploaded
Nice to have
• May have drawings of food in back and white.

```html
<!DOCTYPE html>
<html lang="en">
<head>
<meta charset="utf-8">
<title>Maplebrook Lantern Cafe – Menu</title>
<link rel="stylesheet" href="https://fonts.googleapis.com/css2?family=Great+Vibes&family=Lora:ital,wght@1,400;1,500&family=Montserrat:wght@400;500&family=Dancing+Script:wght@600;700&display=swap">
<style>
:root{
  --brown:#5b423f;
  --brown-soft:#614844;
  --green:#9daa55;
  --white:#ffffff;
  --script:"Great Vibes",cursive;
  --item:"Lora",serif;
  --body:"Montserrat",sans-serif;
  --hand:"Dancing Script",cursive;
}
*{box-sizing:border-box;margin:0;padding:0}
html,body{width:1200px;height:853px;overflow:hidden;background:var(--white)}
.canvas{position:relative;width:1200px;height:853px}
.page{position:absolute;top:35px;width:552px;height:782px;box-shadow:0 2px 10px rgba(0,0,0,.25);overflow:hidden}
.page--outer{left:35px}
.page--inner{left:613px}
.panel{position:absolute;top:0;height:100%}
.panel--brown{background:var(--brown);color:var(--white)}
.panel--green{background:var(--green);color:var(--white)}
.cover{left:0;width:275px}
.cover-art{position:absolute;inset:0;background:var(--brown-soft)}
.brand{position:absolute;left:56px;top:18px;width:162px;height:162px;border-radius:50%;background:var(--white);color:var(--brown);text-align:center;font-family:var(--body)}
.brand-name{margin-top:42px;font-size:15px;font-weight:500;line-height:1.2;color:var(--brown)}
.brand-tag{margin-top:6px;font-size:12px}
.brand-contact{margin-top:14px;font-size:7.5px;line-height:1.5}
.brand-contact strong{font-size:9.5px;font-weight:400}
.info-box{position:absolute;left:17px;top:577px;width:239px;height:141px;border-radius:8px;background:var(--white);color:var(--brown);font-family:var(--hand);font-weight:700;font-size:14.5px;line-height:22px;text-align:center;padding-top:16px;white-space:nowrap}
.heading{position:absolute;display:flex;align-items:center;justify-content:center;font-family:var(--script);font-size:27px;color:var(--white);white-space:nowrap}
.heading svg{position:absolute;inset:0;width:100%;height:100%}
.heading span{position:relative}
.heading--brown svg path{fill:var(--brown)}
.heading--green svg path{fill:var(--green)}
.list{position:absolute}
.row{display:flex;align-items:baseline;height:22px;line-height:22px}
.list--tight .row{height:20.5px;line-height:20.5px}
.name{font-family:var(--item);font-style:italic;font-size:13.5px;letter-spacing:.8px;white-space:nowrap}
.list--tight .name{font-size:12.8px;letter-spacing:.6px}
.dots{flex:1;min-width:10px;border-bottom:1.3px dotted currentColor;margin:0 6px;transform:translateY(-4px);opacity:.9}
.price{font-family:var(--item);font-style:italic;font-size:13px;white-space:nowrap}
.desc{font-family:var(--body);font-size:10.5px;white-space:nowrap}
.desc--sm{font-size:7.6px}
.desc--xs{font-size:5.8px}
.dish{position:absolute;left:13px;width:260px}
.dish .row{height:18px;line-height:18px}
.dish p{font-family:var(--body);font-size:6.8px;line-height:13px;white-space:nowrap}
</style>
</head>
<body>
<div class="canvas">

  <section class="page page--outer">
    <div class="panel panel--brown cover">
      <div class="cover-art" role="img" aria-label="White line drawings of food and drinks: burgers, chicken, tacos, drinks and sandwiches"></div>
      <div class="brand">
        <div class="brand-name">Maplebrook<br>Lantern Cafe</div>
        <div class="brand-tag">Coffee, breakfast &amp; lunch</div>
        <div class="brand-contact">14 Harrow Lane, Elmsdale Q<br><strong>Phone: 07 4000 1234</strong></div>
      </div>
      <div class="info-box">
        14 Harrow Lane, Elmsdale Q 4790<br>
        Phone Orders Welcome! 07 4000 1234<br>
        Open 7 Days From 7am<br>
        Open Weekends<br>
        Saturday &amp; Sunday 7am-12pm
      </div>
    </div>

    <div class="panel panel--green" style="left:275px;width:277px">
      <div class="heading heading--brown" style="left:68px;top:15px;width:140px;height:46px">
        <svg viewBox="0 0 140 46" preserveAspectRatio="none"><path d="M8 4 C40 1 100 2 134 6 C140 18 139 32 136 44 C100 47 40 45 4 42 C0 30 2 14 8 4Z"/></svg><span>Cold Drinks</span>
      </div>
      <div class="list" style="left:20px;top:78px;width:244px">
        <div class="row"><span class="name">Milkshake</span><span class="dots"></span><span class="price">$7.00</span></div>
        <div class="row"><span class="name">Thickshake</span><span class="dots"></span><span class="price">$8.00</span></div>
        <div class="row"><span class="desc desc--sm">Flavours - Chocolate, vanilla, strawberry, banana, caramel &amp; coffee</span></div>
        <div class="row"><span class="name">Iced Latte</span><span class="dots"></span><span class="price">$7.50</span></div>
        <div class="row"><span class="desc" style="font-size:9.3px">Add syrup: vanilla, caramel, white chocolate, hazelnut</span></div>
        <div class="row"><span class="name">Iced Coffee</span><span class="dots"></span><span class="price">$8.00</span></div>
        <div class="row"><span class="name">Iced Chocolate</span><span class="dots"></span><span class="price">$8.00</span></div>
        <div class="row"><span class="name">Iced Mocha</span><span class="dots"></span><span class="price">$8.00</span></div>
      </div>

      <div class="heading heading--brown" style="left:68px;top:285px;width:140px;height:46px">
        <svg viewBox="0 0 140 46" preserveAspectRatio="none"><path d="M8 4 C40 1 100 2 134 6 C140 18 139 32 136 44 C100 47 40 45 4 42 C0 30 2 14 8 4Z"/></svg><span>Juice Bar</span>
      </div>
      <div class="list" style="left:20px;top:348px;width:244px">
        <div class="row"><span class="name">Passion Pop</span><span class="dots"></span><span class="price">$9.00</span></div>
        <div class="row"><span class="desc">Passionfruit, apple &amp; oranges</span></div>
        <div class="row"><span class="name">Sweet Juice</span><span class="dots"></span><span class="price">$9.00</span></div>
        <div class="row"><span class="name">Apple, pineapple, oranges &amp; mango</span></div>
        <div class="row"><span class="name">Orange Juice</span><span class="dots"></span><span class="price">$9.00</span></div>
        <div class="row"><span class="desc">Freshly juiced oranges</span></div>
      </div>

      <div class="heading heading--brown" style="left:68px;top:498px;width:140px;height:46px">
        <svg viewBox="0 0 140 46" preserveAspectRatio="none"><path d="M8 4 C40 1 100 2 134 6 C140 18 139 32 136 44 C100 47 40 45 4 42 C0 30 2 14 8 4Z"/></svg><span>Smoothies</span>
      </div>
      <div class="list" style="left:20px;top:561px;width:244px">
        <div class="row"><span class="name">Mango Raspberry Smoothie</span><span class="dots"></span><span class="price">$9.00</span></div>
        <div class="row"><span class="desc desc--sm">Frozen mango &amp; raspberry sorbet blended with coconut milk</span></div>
        <div class="row"><span class="name">Mango Coconut Smoothie</span><span class="dots"></span><span class="price">$9.00</span></div>
        <div class="row"><span class="desc">Frozen mango blended with coconut milk</span></div>
        <div class="row"><span class="name">Berry Blast Smoothie</span><span class="dots"></span><span class="price">$9.00</span></div>
        <div class="row"><span class="desc">Mixed berries blended with coconut milk</span></div>
        <div class="row"><span class="name">Choc Banana Smoothie</span><span class="dots"></span><span class="price">$9.00</span></div>
        <div class="row"><span class="desc">Frozen banana &amp; dark chocolate ice cream</span></div>
        <div class="row" style="height:18px;line-height:18px"><span class="desc">blended together with whole milk</span></div>
      </div>
    </div>
  </section>

  <section class="page page--inner">
    <div class="panel panel--green" style="left:0;width:274px">
      <div class="heading heading--brown" style="left:68px;top:12px;width:130px;height:45px">
        <svg viewBox="0 0 140 46" preserveAspectRatio="none"><path d="M8 4 C40 1 100 2 134 6 C140 18 139 32 136 44 C100 47 40 45 4 42 C0 30 2 14 8 4Z"/></svg><span>Frappes</span>
      </div>
      <div class="list list--tight" style="left:23px;top:72px;width:232px">
        <div class="row"><span class="name">Strawberry Lemonade Frappe</span><span class="dots"></span><span class="price">$9.00</span></div>
        <div class="row"><span class="desc desc--sm">Strawberry syrup blended together with lemonade &amp; ice</span></div>
        <div class="row"><span class="name">Coffee Frappe</span><span class="dots"></span><span class="price">$9.00</span></div>
        <div class="row"><span class="desc desc--sm" style="font-size:8.2px">Espresso blended with milk &amp; ice, topped with cream</span></div>
        <div class="row"><span class="name">Chocolate Frappe</span></div>
        <div class="row"><span class="desc desc--sm" style="font-size:7.3px">Chocolate syrup blended with milk &amp; ice, topped with cream</span></div>
      </div>

      <div class="heading heading--brown" style="left:68px;top:213px;width:130px;height:45px">
        <svg viewBox="0 0 140 46" preserveAspectRatio="none"><path d="M8 4 C40 1 100 2 134 6 C140 18 139 32 136 44 C100 47 40 45 4 42 C0 30 2 14 8 4Z"/></svg><span>Coffee Menu</span>
      </div>
      <div class="list list--tight" style="left:23px;top:273px;width:222px">
        <div class="row"><span class="name">Cappuccino</span><span class="dots"></span><span class="price">$4.80</span></div>
        <div class="row"><span class="name">Flat White</span><span class="dots"></span><span class="price">$4.80</span></div>
        <div class="row"><span class="name">Latte</span><span class="dots"></span><span class="price">$5.00</span></div>
        <div class="row"><span class="name">Long Black</span><span class="dots"></span><span class="price">$4.80</span></div>
        <div class="row"><span class="name">Mocha</span><span class="dots"></span><span class="price">$5.20</span></div>
        <div class="row"><span class="name">Macchiato</span><span class="dots"></span><span class="price">$3.50</span></div>
        <div class="row"><span class="name">Espresso</span><span class="dots"></span><span class="price">$3.50</span></div>
        <div class="row"><span class="name">Chai Latte</span><span class="dots"></span><span class="price">$4.80</span></div>
        <div class="row"><span class="name">Hot Chocolate</span><span class="dots"></span><span class="price">$4.80</span></div>
        <div class="row"><span class="name">Tea</span><span class="dots"></span><span class="price">$4.50</span></div>
        <div class="row"><span class="desc desc--xs">Tea Flavours: English breakfast, earl grey, green, berry green &amp; coconut</span></div>
      </div>

      <div class="heading heading--brown" style="left:55px;top:516px;width:156px;height:44px">
        <svg viewBox="0 0 140 46" preserveAspectRatio="none"><path d="M8 4 C40 1 100 2 134 6 C140 18 139 32 136 44 C100 47 40 45 4 42 C0 30 2 14 8 4Z"/></svg><span>Takeaway Coffee</span>
      </div>
      <div class="list list--tight" style="left:23px;top:575px;width:222px">
        <div class="row"><span class="name">Takeaway Large</span><span class="dots"></span><span class="price">$6.80</span></div>
        <div class="row"><span class="name">Takeaway Regular</span><span class="dots"></span><span class="price">$5.20</span></div>
        <div class="row"><span class="name">Takeaway Small</span><span class="dots"></span><span class="price">$4.80</span></div>
      </div>

      <div class="heading heading--brown" style="left:55px;top:652px;width:156px;height:44px">
        <svg viewBox="0 0 140 46" preserveAspectRatio="none"><path d="M8 4 C40 1 100 2 134 6 C140 18 139 32 136 44 C100 47 40 45 4 42 C0 30 2 14 8 4Z"/></svg><span>Coffee Extras</span>
      </div>
      <div class="list list--tight" style="left:23px;top:711px;width:227px">
        <div class="row"><span class="name">Mug &amp; Extra Shot</span><span class="dots"></span><span class="price">50c</span></div>
        <div class="row"><span class="name">Soy &amp; Lactose Free Milk</span><span class="dots"></span><span class="price">80c</span></div>
        <div class="row"><span class="name">Syrups</span><span class="dots"></span><span class="price">$1.00</span></div>
      </div>
    </div>

    <div class="panel panel--brown" style="left:274px;width:278px">
      <div class="heading heading--green" style="left:68px;top:15px;width:140px;height:46px">
        <svg viewBox="0 0 140 46" preserveAspectRatio="none"><path d="M8 4 C40 1 100 2 134 6 C140 18 139 32 136 44 C100 47 40 45 4 42 C0 30 2 14 8 4Z"/></svg><span>Kids Menu</span>
      </div>
      <div class="list" style="left:20px;top:78px;width:244px">
        <div class="row"><span class="name">Scrambled Eggs</span><span class="dots"></span><span class="price">$9.50</span></div>
        <div class="row"><span class="desc" style="font-size:9.6px">Two eggs scrambled with toast &amp; tomato sauce</span></div>
        <div class="row"><span class="name">Rainbow Pancakes</span><span class="dots"></span><span class="price">$9.50</span></div>
        <div class="row"><span class="desc" style="font-size:8.6px">Two small pancakes served with ice cream &amp; sprinkles</span></div>
        <div class="row"><span class="name">Nuggets &amp; Chips</span><span class="dots"></span><span class="price">$8.00</span></div>
        <div class="row"><span class="name">Chicken Chippees</span><span class="dots"></span><span class="price">$8.50</span></div>
      </div>

      <div class="heading heading--green" style="left:53px;top:238px;width:173px;height:46px">
        <svg viewBox="0 0 140 46" preserveAspectRatio="none"><path d="M8 4 C40 1 100 2 134 6 C140 18 139 32 136 44 C100 47 40 45 4 42 C0 30 2 14 8 4Z"/></svg><span>Breakfast Menu</span>
      </div>

      <div class="dish" style="top:303px">
        <div class="row"><span class="name">Big Breakfast</span><span class="dots"></span><span class="price">$21.50</span></div>
        <p>Bacon, sausages, hash browns, tomato, baked beans &amp; mushrooms<br>with a slice of toasted panini bread &amp; your choice of fried,<br>poached or scrambled eggs.</p>
      </div>
      <div class="dish" style="top:363px">
        <div class="row"><span class="name">Classic Breakfast</span><span class="dots"></span><span class="price">$16.500</span></div>
        <p>Your choice of fried poached or scrambled eggs served with either<br>bacon or sausages, tomato &amp; a slice of panini toast</p>
      </div>
      <div class="dish" style="top:412px">
        <div class="row"><span class="name">Avocado Stack</span><span class="dots"></span><span class="price">$17.00</span></div>
        <p>Turkish bread topped with avocado, bacon or salmon, 2 poached<br>eggs &amp; a sprinkle of feta cheese poached or scrambled eggs.</p>
      </div>
      <div class="dish" style="top:463px">
        <div class="row"><span class="name">Eggs Benedict</span><span class="dots"></span><span class="price">$19.00</span></div>
        <p>Your choice of bacon, ham or salmon served with toasted turkish<br>bread, poached eggs &amp; creamy hollandaise sauce</p>
      </div>
      <div class="dish" style="top:512px">
        <div class="row"><span class="name">Classic Omelet</span><span class="dots"></span><span class="price">$17.50</span></div>
        <p>Ham, tomato, spinach, onion &amp; cheese omelet topped with fried cherry<br>tomatoes &amp; turkish toast</p>
      </div>
      <div class="dish" style="top:561px">
        <div class="row"><span class="name">Panini Scramble</span><span class="dots"></span><span class="price">$16.50</span></div>
        <p>Toasted panini bread topped with scrambled eggs, sautéed<br>mushrooms, cherry tomatoes &amp; spinach with a drizzle of hollandaise<br>sauce on top</p>
      </div>
      <div class="dish" style="top:624px">
        <div class="row"><span class="name">Breaky Wrap</span><span class="dots"></span><span class="price">$15.00</span></div>
        <p>Bacon, eggs, hash browns, cheese &amp; BBQ sauce on a toasted wrap</p>
      </div>
      <div class="dish" style="top:675px">
        <div class="row"><span class="name">Ultimate Breakfast Toastie</span><span class="dots"></span><span class="price">$14.50</span></div>
        <p>Bacon, scrambled eggs, smashed avocado, spinach &amp; feta with<br>hollandaise sauce on a toasted ciabatta sandwich roll</p>
      </div>
      <div class="dish" style="top:726px">
        <div class="row"><span class="name">Breakfast Share Plate</span><span class="dots"></span><span class="price">$28.50</span></div>
        <p>A delicious selection of yummy breakfast items including bacon,<br>scrambled eggs, hash browns, croissant, yogurt, strawberries &amp;</p>
      </div>
    </div>
  </section>

</div>
</body>
</html>
```